Facebook Banner

Hi, I need help making banners for my social media channels. Once we make one banner all the other banners will follow the same look and feel. Please help me design my Facebook page banner to start.

Attached is my branding guidelines - please choose a design that fits within my Branding Guidelines. Please note that I only use two fonts. Belanosima and Arial. I have also attached screenshots of my Youtube channel and Tiktok thumbnails. I made banners already but I am not happy with them. Please take into account my whole “brand universe” to create the banner.

The message I want to convey in the banner is that I offer tours of factories in Vietnam. I offer to take clients on factory tours and the tours include car, driver and translator.

If you have any questions then please don't hesitate to ask.

I have included images of factory tours. I also included my logo in case you want to use it.

```html
<!DOCTYPE html>
<html lang="en">
<head>
<meta charset="utf-8">
<title>Facebook Cover – Factory Visits</title>
<link href="https://fonts.googleapis.com/css2?family=Poppins:wght@500;600;700&display=swap" rel="stylesheet">
<style>
  :root {
    --page-bg: #161c26;
    --cover-bg: #2a0a35;
    --ring-deep: #5a1042;
    --magenta: #8c1650;
    --magenta-bright: #a3195b;
    --ring-line: #b8306f;
    --white: #ffffff;
    --photo-light: #8a8a8a;
    --photo-dark: #2b2b2b;
  }
  html, body {
    margin: 0;
    padding: 0;
    width: 1200px;
    height: 1200px;
    overflow: hidden;
    background: var(--page-bg);
  }
  .cover {
    position: absolute;
    left: 0;
    top: 380px;
    width: 1200px;
    height: 441px;
  }
  .cover svg { display: block; }
  .headline {
    font-family: "Poppins", Arial, sans-serif;
    font-weight: 500;
    font-size: 54px;
    fill: var(--white);
  }
  .headline .accent {
    font-weight: 700;
    fill: var(--magenta-bright);
  }
  .services-text {
    font-family: "Poppins", Arial, sans-serif;
    font-weight: 600;
    font-size: 18px;
    letter-spacing: 1.2px;
    fill: var(--white);
  }
  .brand-name {
    font-family: "Poppins", Arial, sans-serif;
    font-weight: 600;
    font-size: 27px;
    fill: var(--white);
  }
</style>
</head>
<body>
<div class="cover">
  <svg width="1200" height="441" viewBox="0 0 1200 441" xmlns="http://www.w3.org/2000/svg">
    <defs>
      <linearGradient id="left-glow" x1="0" y1="0" x2="1" y2="0">
        <stop offset="0" stop-color="#5a1446" stop-opacity="0.8"/>
        <stop offset="1" stop-color="#2a0a35" stop-opacity="0"/>
      </linearGradient>
      <linearGradient id="photo-tone" x1="0" y1="0" x2="0" y2="1">
        <stop offset="0" stop-color="var(--photo-light)"/>
        <stop offset="1" stop-color="var(--photo-dark)"/>
      </linearGradient>
      <clipPath id="cover-clip"><rect width="1200" height="441"/></clipPath>
    </defs>

    <g clip-path="url(#cover-clip)">
      <rect class="backdrop" width="1200" height="441" fill="var(--cover-bg)"/>
      <rect class="backdrop-glow" width="330" height="441" fill="url(#left-glow)"/>

      <!-- central rings behind the portrait -->
      <circle class="ring-outer" cx="697" cy="225" r="249" fill="var(--ring-deep)"/>
      <circle class="ring-inner" cx="697" cy="225" r="168" fill="var(--magenta)"/>

      <!-- top accent circle -->
      <circle class="accent-circle" cx="457" cy="60" r="96" fill="var(--magenta)"/>
      <circle class="accent-outline" cx="457" cy="60" r="117" fill="none" stroke="var(--ring-line)" stroke-width="2"/>

      <!-- bottom-right accent circle -->
      <circle class="accent-circle" cx="943" cy="379" r="96" fill="var(--magenta)"/>
      <circle class="accent-outline" cx="943" cy="379" r="117" fill="none" stroke="var(--ring-line)" stroke-width="2"/>

      <!-- portrait -->
      <path class="portrait" role="img" aria-label="Black-and-white photo of the tour guide standing with arms crossed"
            d="M650 60 Q650 12 697 12 Q744 12 744 60 L744 120 Q800 150 845 200 L850 441 L548 441 L552 200 Q595 150 650 120 Z"
            fill="url(#photo-tone)"/>
    </g>

    <!-- headline -->
    <text class="headline">
      <tspan x="111" y="200">VISIT</tspan>
      <tspan x="111" y="256">FACTORIES</tspan>
      <tspan x="111" y="312">IN <tspan class="accent">VIETNAM</tspan></tspan>
    </text>

    <!-- services pill -->
    <rect class="services-pill" x="108" y="331" width="329" height="36" rx="18" fill="var(--magenta)"/>
    <text class="services-text" x="272.5" y="355.5" text-anchor="middle">CAR • DRIVER • TRANSLATOR</text>

    <!-- brand name -->
    <text class="brand-name" text-anchor="end">
      <tspan x="1147" y="88">LOTUS PLANT</tspan>
      <tspan x="1147" y="118">VISITS</tspan>
    </text>
  </svg>
</div>
</body>
</html>
```